Highly motivated family winery needs new wine labels.

Company and target group:
We are a smaller, family-run winery in the heart of Germany and focus on quality rather than quantity. We primarily market to private customers, but are also represented in food retail. The wines appeal to both younger and older wine drinkers (30 – 80 years old). The labels should also be accordingly.
Requirements and wishes:
We would like to have a new logo consisting of the letters F and W that can be used in both 1 color and 2 colors. The family name “Weidlinger” should appear on the label, with the font being left to the creativity of the designers. The size of the label has not yet been fixed, but it should run around the bottle and therefore have a front and back (around 160mm wide and 80mm high). The design should be simple, modern and not too ornate.
The currently 22 types of wine/sparkling wine should all have the same label, but we would like to color-code the flavors in some way.
Perhaps the silhouette of one of the buildings of our winery (with the tower) can be incorporated into the design of the label (see picture).
A central element of the labels should have a high recognition value and be placed on the front of the label with the later wine type information.
We look forward to your suggestions.
Wegen der Weihnachtsfeiertage möchte ich das Projekt verlängern, um den Designern mehr Zeit zu geben. Bisher sind auch nur wenige Worschläge eingegangen.

```html
<!DOCTYPE html>
<html lang="de">
<head>
<meta charset="utf-8">
<title>Weidlinger – Weinetikett</title>
<link rel="stylesheet" href="https://fonts.googleapis.com/css2?family=Anton&family=Oswald:wght@500&display=swap">
<style>
  :root {
    --canvas-bg: #ececec;
    --label-bg: #f7f7f7;
    --contour-tone: #ebebeb;
    --ink: #111111;
    --accent-red: #e2404d;
    --logo-red: #d8242f;
    --white: #ffffff;
    --photo-tone: #8d8a86;
  }
  * { margin: 0; padding: 0; box-sizing: border-box; }
  html, body {
    width: 866px;
    height: 1200px;
    overflow: hidden;
    background: var(--canvas-bg);
  }
  .canvas {
    position: relative;
    width: 866px;
    height: 1200px;
    display: flex;
    align-items: center;
    justify-content: center;
  }
  .wine-label {
    position: relative;
    width: 700px;
    height: 672px;
    background: var(--label-bg);
    overflow: hidden;
    box-shadow: 0 2px 14px rgba(0,0,0,0.08);
  }
  .contour-texture {
    position: absolute;
    inset: 0;
    background: radial-gradient(ellipse at 70% 30%, var(--contour-tone), var(--label-bg) 70%);
  }
  .brand-bar {
    position: absolute;
    left: 0;
    top: 48px;
    width: 406px;
    height: 112px;
    background: var(--ink);
    display: flex;
    align-items: center;
    justify-content: flex-end;
  }
  .brand-mark {
    width: 148px;
    height: 100%;
    background: var(--white);
    display: flex;
    align-items: center;
    justify-content: center;
    font-family: "Oswald", sans-serif;
    font-weight: 500;
    font-size: 64px;
    color: var(--logo-red);
    letter-spacing: 2px;
  }
  .family-name {
    position: absolute;
    left: 196px;
    top: 330px;
    right: 0;
  }
  .name-top {
    display: flex;
    align-items: flex-end;
    gap: 14px;
    height: 112px;
  }
  .name-top-text {
    font-family: "Anton", sans-serif;
    font-size: 118px;
    line-height: 0.95;
    color: var(--ink);
    letter-spacing: 1px;
  }
  .winery-photo {
    width: 120px;
    height: 84px;
    margin-bottom: 8px;
    background: linear-gradient(180deg, #b9b6b2, var(--photo-tone) 60%, #4f4c48);
  }
  .name-band {
    margin-left: -14px;
    margin-top: 4px;
    height: 118px;
    background: var(--accent-red);
    display: flex;
    align-items: center;
    padding-left: 14px;
  }
  .name-band-text {
    font-family: "Anton", sans-serif;
    font-size: 112px;
    line-height: 1;
    color: var(--white);
    letter-spacing: 1px;
  }
</style>
</head>
<body>
  <main class="canvas">
    <section class="wine-label">
      <div class="contour-texture" role="img" aria-label="Dezentes Höhenlinien-Muster als Etiketthintergrund"></div>
      <div class="brand-bar">
        <div class="brand-mark">FW</div>
      </div>
      <div class="family-name">
        <div class="name-top">
          <span class="name-top-text">WEID</span>
          <div class="winery-photo" role="img" aria-label="Foto des Weinguts mit Turm"></div>
        </div>
        <div class="name-band">
          <span class="name-band-text">LINGER</span>
        </div>
      </div>
    </section>
  </main>
</body>
</html>
```